Business Card Design

We need a business card for a well established Semi Trailer Hire company. I am looking for a new start as we are moving so would like to update our Business Cards and Letter heads.
We hire Semi Trailers to Transport companies.
The colour of our Trailers are Cherry Red so this must be the prominent colour.
I do not want any pictures of trailers on the design.
I do not want the design to be flowery in anyway as we are in the transport industry.
Simple yet effective

Trovan Hire Pty Ltd
Ros Dunmore
Director
Ph: 03 9412 5083
Mobile: 0421 736 209
ros.dunmore@trovanhire.com.au
www.trovanhire.com.au
214-220 Pellow Road, Ashcombe

```html
<!DOCTYPE html>
<html lang="en">
<head>
<meta charset="utf-8">
<title>Trovan Hire Pty Ltd – Business Card</title>
<link rel="stylesheet" href="https://fonts.googleapis.com/css2?family=Cinzel:wght@400;600&display=swap">
<style>
  :root {
    --cherry: #a3141f;
    --cherry-deep: #6e0a12;
    --cherry-bright: #c21d29;
    --paper: #ffffff;
    --paper-shade: #e9e9ea;
    --ink-grey: #6f6f72;
    --backdrop: #e7e4df;
  }
  * { margin: 0; padding: 0; box-sizing: border-box; }
  html, body {
    width: 1200px; height: 600px; overflow: hidden;
    background: var(--backdrop);
    font-family: "Cinzel", serif;
  }
  .stage {
    width: 1200px; height: 600px;
    display: flex; align-items: center; justify-content: center; gap: 60px;
  }
  .card {
    position: relative; width: 510px; height: 292px;
    box-shadow: 0 10px 28px rgba(0,0,0,0.22), 0 2px 6px rgba(0,0,0,0.15);
  }
  .card--front {
    background: linear-gradient(135deg, var(--paper) 0%, var(--paper) 55%, var(--paper-shade) 100%);
    padding: 0 34px;
  }
  .card__head {
    position: absolute; left: 34px; right: 34px; top: 96px;
    display: flex; justify-content: space-between; align-items: flex-end;
  }
  .company-name {
    color: var(--cherry); font-size: 25px; font-weight: 600; letter-spacing: 0.5px;
    line-height: 1;
  }
  .person { text-align: right; }
  .person__name {
    color: var(--cherry); font-size: 15px; font-weight: 600; line-height: 1.1;
  }
  .person__role {
    color: var(--ink-grey); font-size: 9.5px; letter-spacing: 1px; margin-top: 3px;
  }
  .divider {
    position: absolute; left: 34px; right: 34px; top: 138px;
    height: 1.5px; background: var(--cherry);
  }
  .card__foot {
    position: absolute; left: 34px; right: 34px; top: 160px;
    display: flex; justify-content: space-between; align-items: flex-start;
  }
  .contacts {
    list-style: none;
    color: var(--ink-grey); font-size: 9.5px; letter-spacing: 0.5px; line-height: 1.7;
  }
  .contacts li { display: flex; align-items: center; gap: 7px; }
  .contacts svg { width: 10px; height: 10px; flex: none; }
  .address {
    text-align: right; font-style: normal;
    color: var(--ink-grey); font-size: 9.5px; letter-spacing: 0.6px; line-height: 1.7;
  }
  .card--back {
    background: radial-gradient(ellipse at 45% 35%, var(--cherry-bright) 0%, var(--cherry) 45%, var(--cherry-deep) 100%);
    display: flex; align-items: center; justify-content: center;
  }
  .card--back .company-name { color: var(--paper); font-size: 26px; }
</style>
</head>
<body>
<main class="stage">
  <section class="card card--front" aria-label="Business card front">
    <div class="card__head">
      <h1 class="company-name">Trovan Hire Pty Ltd</h1>
      <div class="person">
        <p class="person__name">Ros Dunmore</p>
        <p class="person__role">Director</p>
      </div>
    </div>
    <div class="divider"></div>
    <div class="card__foot">
      <ul class="contacts">
        <li>
          <svg viewBox="0 0 10 10" aria-hidden="true"><rect width="10" height="10" fill="var(--cherry)"/><path d="M3 2.2h1.2l.6 1.5-.8.6c.4.9 1 1.5 1.9 1.9l.6-.8 1.5.6V7.2c0 .4-.3.6-.7.6C4.6 7.6 2.4 5.4 2.3 2.9c0-.4.3-.7.7-.7z" fill="#fff"/></svg>
          03 9412 5083
        </li>
        <li>
          <svg viewBox="0 0 10 10" aria-hidden="true"><rect width="10" height="10" fill="var(--cherry)"/><rect x="3.3" y="1.8" width="3.4" height="6.4" rx="0.5" fill="#fff"/><rect x="3.9" y="2.6" width="2.2" height="4" fill="var(--cherry)"/></svg>
          0421 736 209
        </li>
        <li>
          <svg viewBox="0 0 10 10" aria-hidden="true"><rect width="10" height="10" fill="var(--cherry)"/><rect x="2" y="3" width="6" height="4.2" fill="#fff"/><path d="M2 3l3 2.4L8 3" fill="none" stroke="var(--cherry)" stroke-width="0.7"/></svg>
          ros.dunmore@trovanhire.com.au
        </li>
        <li>
          <svg viewBox="0 0 10 10" aria-hidden="true"><rect width="10" height="10" fill="var(--cherry)"/><circle cx="5" cy="5" r="2.8" fill="none" stroke="#fff" stroke-width="0.7"/><path d="M2.2 5h5.6M5 2.2c-1.4 1.6-1.4 4 0 5.6M5 2.2c1.4 1.6 1.4 4 0 5.6" fill="none" stroke="#fff" stroke-width="0.6"/></svg>
          www.trovanhire.com.au
        </li>
      </ul>
      <address class="address">214-220 Pellow Road<br>Ashcombe</address>
    </div>
  </section>

  <section class="card card--back" aria-label="Business card back">
    <h2 class="company-name">Trovan Hire Pty Ltd</h2>
  </section>
</main>
</body>
</html>
```